Website - Tides Of Bloom

We are catalysts of change in people's lives.
We work with individuals and professionals to bring about instant substantial & transforming change in their lives.
We provide one-on-one lifestyle coaching by an experienced practitioner.
Our existing website is www.tidesofbloom.biz & this site contains our the basis for the content of our desired new project, so please examine this carefully.
We require a professional and captivating website that will instantly impress, engage invite our readers to click & invest their lives.
Our services do not come cheap, but are second to none.
Our website must be contemporary whilst reflecting indisputable class & ultra-confidence in the success of our work.
Target Market(s)
Those who seek to want to change in their lives. Those aged primarily between 30 and 50 years of age, male or female.
Industry/Entity Type
Work
Look and feel

```html
<!DOCTYPE html>
<html lang="en">
<head>
<meta charset="utf-8">
<title>Tides Of Bloom — Contact</title>
<link rel="stylesheet" href="https://fonts.googleapis.com/css2?family=Open+Sans:wdth,wght@75..100,300..800&display=swap">
<style>
  :root {
    --lime: #8dc31e;
    --orange: #f06a10;
    --white: #ffffff;
    --panel: rgba(12, 38, 58, 0.62);
    --sky-top: #1b6fb4;
    --sky-mid: #4c9fd6;
    --sea: #2c4f66;
    --sea-deep: #1d3547;
    --link: #9fd0f0;
    --muted: #d5dde3;
    --field-text: #b5b5b5;
    --map-land: #efeae0;
    --map-water: #aacbe6;
  }
  * { box-sizing: border-box; margin: 0; padding: 0; }
  html, body { width: 1200px; height: 1000px; overflow: hidden; background: var(--white); }
  body { font-family: "Open Sans", sans-serif; color: var(--white); position: relative; }

  .stage {
    position: absolute; left: 0; top: 162px; width: 1200px; height: 823px;
    border-top: 8px solid var(--lime); border-bottom: 7px solid var(--lime);
  }
  .hero-photo {
    position: absolute; inset: 0;
    background: linear-gradient(180deg, var(--sky-top) 0%, var(--sky-mid) 48%, var(--sea) 62%, var(--sea-deep) 100%);
  }
  .content-panel {
    position: absolute; left: 91px; top: 0; width: 1025px; height: 100%;
    background: var(--panel);
  }
  .sound-toggle {
    position: absolute; left: 91px; top: 0; width: 20px; height: 19px;
    background: var(--lime); display: flex; align-items: center; justify-content: center;
  }
  .menu-tab {
    position: absolute; left: 5px; top: 363px; width: 37px; height: 97px;
    background: rgba(20, 40, 50, 0.85); border-left: 4px solid var(--lime);
    display: flex; align-items: center; justify-content: center;
  }
  .menu-tab span {
    transform: rotate(-90deg); font-size: 27px; font-weight: 400; letter-spacing: 0.5px; white-space: nowrap;
  }
  .brand {
    position: absolute; left: 810px; top: 32px; display: flex; align-items: center; gap: 14px;
  }
  .brand-dot { width: 46px; height: 46px; border-radius: 50%; background: var(--lime); }
  .brand-name { font-size: 30px; font-weight: 600; font-stretch: 75%; line-height: 1; color: var(--muted); }

  .section-head {
    position: absolute; left: 140px; width: 926px; height: 34px;
    border-bottom: 1px solid var(--lime); display: flex; align-items: flex-end;
  }
  .step-num {
    width: 24px; height: 33px; background: var(--lime); font-size: 20px; font-weight: 300;
    display: flex; align-items: center; justify-content: center;
  }
  .section-title { margin-left: 8px; font-size: 22px; font-weight: 300; line-height: 33px; }
  .section-title strong { font-weight: 600; }

  .contact-phone {
    position: absolute; left: 140px; top: 213px; font-size: 33px; font-weight: 700; font-stretch: 75%; line-height: 1;
  }
  .contact-email { position: absolute; left: 140px; top: 243px; font-size: 16px; color: var(--link); }
  .contact-address { position: absolute; left: 140px; top: 266px; font-size: 12px; font-weight: 300; color: var(--muted); }

  .field {
    position: absolute; background: var(--white); color: var(--field-text);
    font-size: 12px; padding: 7px 6px; border: 1px solid #dcdcdc;
  }
  .send-btn {
    position: absolute; left: 140px; top: 578px; width: 80px; height: 31px; background: var(--lime);
    font-size: 19px; font-weight: 300; font-stretch: 75%; display: flex; align-items: center; justify-content: center;
  }
  .map {
    position: absolute; left: 140px; top: 751px; width: 926px; height: 57px;
    background: linear-gradient(90deg, var(--map-land) 0%, var(--map-land) 70%, var(--map-water) 100%);
  }
  .map-types { position: absolute; right: 11px; top: 11px; display: flex; }
  .map-types span {
    background: var(--white); color: #222; border: 1px solid #777; font-size: 11px;
    padding: 1px 10px; margin-left: 2px;
  }
  .map-types span.active { font-weight: 700; }
  .page-counter {
    position: absolute; left: 92px; top: 772px; font-size: 36px; font-weight: 700; font-stretch: 75%; line-height: 1;
  }
  .page-counter em { font-style: normal; color: var(--orange); }
  .fullscreen-toggle {
    position: absolute; left: 1098px; top: 788px; width: 18px; height: 20px; background: var(--lime);
    display: flex; align-items: center; justify-content: center;
  }
</style>
</head>
<body>
  <main class="stage">
    <div class="hero-photo" role="img" aria-label="Photo of a man with outstretched arms on a sunny beach, sea and blue sky behind"></div>
    <section class="content-panel">
      <div class="brand"><span class="brand-dot"></span><span class="brand-name">Tides Of Bloom</span></div>

      <div class="section-head" style="top:159px"><span class="step-num">1</span><h2 class="section-title"><strong>Email or call us</strong> // Use our number to get in touch</h2></div>
      <div class="contact-phone">+61 02 5550 1274</div>
      <div class="contact-email">contact@tidesofbloom.biz</div>
      <div class="contact-address">Address line 1, str. Generic, no.10, LoremIpsum, CA</div>

      <div class="section-head" style="top:370px"><span class="step-num">2</span><h2 class="section-title"><strong>Leave a message</strong> // Use our contact form to write us</h2></div>
      <div class="field" style="left:140px;top:424px;width:207px;height:31px">Name</div>
      <div class="field" style="left:367px;top:424px;width:207px;height:31px">Website</div>
      <div class="field" style="left:140px;top:475px;width:207px;height:31px">Email</div>
      <div class="field" style="left:367px;top:475px;width:207px;height:31px">Phone No</div>
      <div class="field" style="left:604px;top:424px;width:384px;height:134px">Type your message here...</div>
      <div class="send-btn">Send</div>

      <div class="section-head" style="top:697px"><span class="step-num">3</span><h2 class="section-title"><strong>Visit us</strong> // Use the map to locate us</h2></div>
      <div class="map" role="img" aria-label="Street map showing the office location">
        <div class="map-types"><span class="active">Map</span><span>Sat</span><span>Ter</span><span>Earth</span></div>
      </div>
    </section>

    <div class="sound-toggle">
      <svg width="12" height="11" viewBox="0 0 12 11"><path d="M1 4h2l3-3v9L3 7H1z" fill="#fff"/><path d="M8 3.5q1.5 2 0 4M9.5 2q2.5 3.5 0 7" stroke="#fff" stroke-width="1" fill="none"/></svg>
    </div>
    <nav class="menu-tab"><span>menu</span></nav>
    <div class="page-counter">06/<em>01</em></div>
    <div class="fullscreen-toggle">
      <svg width="12" height="12" viewBox="0 0 12 12"><rect x="1" y="4" width="7" height="7" fill="none" stroke="#fff"/><path d="M6 6l5-5M7 1h4v4" stroke="#fff" fill="none"/></svg>
    </div>
  </main>
</body>
</html>
```